Whitening Flyer

I need an informational flyer for my dental practice. The flyer will describe the whitening services that are available at my practice and show price of each whitening service. We currently gave a 3 fold brochure, but I prefer something with a more professional look, and personalized with our branding and practice colors. I have attached the current flyer for you to use similar text. I will also attach a flyer that I have used in the past that could demonstrate my branding or feel free to view my website: www.pemtrix.com

```html
<!DOCTYPE html>
<html lang="en">
<head>
<meta charset="utf-8">
<title>Smileform Dental – Teeth Whitening Brochure</title>
<link rel="stylesheet" href="https://fonts.googleapis.com/css2?family=Montserrat:ital,wght@0,400;0,500;0,600;0,700;0,800;0,900;1,400&display=swap">
<style>
  :root {
    --brand-red: #c8202a;
    --brand-red-dark: #a8161f;
    --paper: #ffffff;
    --ink: #1d1d1f;
    --ink-soft: #3b3b3f;
    --stage: #e4e4e6;
    --pill-grey: #ececec;
    --price-black: #111111;
    --gold: #f2c230;
    --diamond: #e9d9b8;
    --platinum: #9fd0ea;
  }
  * { box-sizing: border-box; margin: 0; padding: 0; }
  html, body { width: 1200px; height: 2400px; overflow: hidden; }
  body {
    background: var(--stage);
    font-family: "Montserrat", Arial, sans-serif;
    color: var(--ink);
    position: relative;
  }
  .spread {
    position: absolute;
    left: 50px;
    width: 1100px;
    height: 850px;
    background: var(--paper);
    box-shadow: 0 10px 30px rgba(0,0,0,.12);
    overflow: hidden;
  }
  .spread--outside { top: 250px; }
  .spread--inside { top: 1300px; }
  .spread > svg.spread__art { position: absolute; inset: 0; }
  .abs { position: absolute; }

  /* ---------- outside: about panel ---------- */
  .rank { left: 30px; top: 36px; display: flex; align-items: center; gap: 6px; color: var(--brand-red); }
  .rank__number { font-size: 42px; font-weight: 900; line-height: 1; }
  .rank__label { font-size: 12px; font-weight: 800; line-height: 1.2; text-transform: uppercase; font-style: italic; }
  .about-copy { left: 30px; top: 104px; width: 306px; font-size: 12.5px; line-height: 1.5; font-style: italic; color: var(--ink-soft); text-align: justify; }
  .mission { left: 64px; top: 318px; width: 240px; color: var(--paper); text-align: center; }
  .mission__title { font-size: 13px; font-weight: 800; letter-spacing: .5px; margin-bottom: 8px; }
  .mission__copy { font-size: 10.5px; line-height: 1.5; font-style: italic; text-align: justify; }

  /* ---------- outside: contact panel ---------- */
  .contact { left: 367px; top: 52px; width: 366px; text-align: center; }
  .contact__call { color: var(--brand-red); font-size: 15px; font-weight: 800; text-transform: uppercase; }
  .contact__phone { display: inline-block; margin-top: 6px; background: var(--brand-red); color: var(--paper); font-size: 23px; font-weight: 800; padding: 6px 22px; border-radius: 12px; letter-spacing: .5px; }
  .contact__details { margin-top: 58px; font-size: 13.5px; font-weight: 600; line-height: 1.55; color: var(--ink); }
  .contact__details p + p { margin-top: 10px; }
  .brand { display: flex; align-items: center; justify-content: center; gap: 8px; font-weight: 700; }
  .brand__dot { width: 12px; height: 12px; border-radius: 50%; background: currentColor; }
  .brand--back { left: 367px; width: 366px; top: 730px; color: var(--paper); font-size: 24px; }

  /* ---------- outside: cover panel ---------- */
  .brand--cover { left: 733px; width: 367px; top: 48px; color: var(--brand-red); font-size: 27px; }
  .cover-headline { left: 733px; width: 367px; top: 548px; text-align: center; color: var(--paper); }
  .cover-headline__lead { font-size: 19px; font-weight: 600; letter-spacing: 1px; text-transform: uppercase; }
  .cover-headline__main { font-size: 74px; font-weight: 800; line-height: 1; letter-spacing: 1px; }
  .cover-web { left: 773px; width: 287px; top: 700px; height: 46px; background: var(--pill-grey); border-radius: 12px; display: flex; align-items: center; justify-content: center; font-size: 15px; font-weight: 700; letter-spacing: 5px; color: var(--ink); }

  /* ---------- inside: intro panel ---------- */
  .services-title { left: 36px; top: 36px; color: var(--brand-red); font-size: 30px; font-weight: 800; line-height: 1.08; text-transform: uppercase; }
  .services-copy { left: 36px; top: 156px; width: 296px; font-size: 11.5px; line-height: 1.45; color: var(--ink-soft); }

  /* ---------- inside: price list ---------- */
  .tier { width: 320px; color: var(--paper); display: grid; grid-template-columns: 64px 1fr; column-gap: 6px; }
  .tier__badge { grid-row: 1 / span 2; width: 58px; height: 58px; border-radius: 50%; background: var(--price-black); display: flex; align-items: center; justify-content: center; font-size: 17px; font-weight: 800; line-height: 1; border: 3px solid var(--paper); }
  .tier__badge--basic { color: var(--brand-red); }
  .tier__badge--gold { color: var(--gold); border: 3px dashed var(--gold); }
  .tier__badge--silver { color: var(--paper); }
  .tier__badge--diamond { color: var(--diamond); }
  .tier__badge--platinum { color: var(--platinum); }
  .tier__name { font-size: 22px; font-weight: 800; line-height: 1; text-transform: uppercase; }
  .tier__kind { font-size: 11.5px; font-weight: 500; line-height: 1.2; text-transform: uppercase; }
  .tier__copy { grid-column: 1 / span 2; margin-top: 10px; font-size: 10.5px; line-height: 1.45; }
  .tier--basic { left: 395px; top: 338px; }
  .tier--gold { left: 395px; top: 530px; }
  .tier--silver { left: 762px; top: 330px; }
  .tier--diamond { left: 762px; top: 480px; }
  .tier--platinum { left: 762px; top: 630px; }
  .closing-call { left: 367px; width: 366px; top: 806px; text-align: center; color: var(--brand-red); font-size: 22px; font-weight: 800; text-transform: uppercase; }
  .closing-phone { left: 733px; width: 367px; top: 804px; text-align: center; color: var(--ink); font-size: 26px; font-weight: 800; letter-spacing: .5px; }
</style>
</head>
<body>

<!-- ============ OUTSIDE SPREAD ============ -->
<section class="spread spread--outside" aria-label="Brochure outside">
  <svg class="spread__art" viewBox="0 0 1100 850" width="1100" height="850">
    <defs>
      <linearGradient id="portraitWarm" x1="0" y1="0" x2="1" y2="1">
        <stop offset="0" stop-color="#3a241b"/>
        <stop offset=".55" stop-color="#8a5a43"/>
        <stop offset="1" stop-color="#e9e4df"/>
      </linearGradient>
      <linearGradient id="portraitLight" x1="0" y1="0" x2="0" y2="1">
        <stop offset="0" stop-color="#2a1c18"/>
        <stop offset=".6" stop-color="#a87a62"/>
        <stop offset="1" stop-color="#f1eeec"/>
      </linearGradient>
      <linearGradient id="mapTone" x1="0" y1="0" x2="1" y2="1">
        <stop offset="0" stop-color="#f1efe9"/>
        <stop offset="1" stop-color="#dcdcd6"/>
      </linearGradient>
    </defs>

    <!-- panel folds -->
    <line x1="367" y1="0" x2="367" y2="850" stroke="#e2e2e2" stroke-width="1"/>
    <line x1="733" y1="0" x2="733" y2="850" stroke="#e2e2e2" stroke-width="1"/>

    <!-- about panel: mission card and portrait -->
    <rect x="44" y="290" width="280" height="350" rx="40" fill="var(--brand-red)"/>
    <rect x="20" y="672" width="200" height="168" rx="18" fill="url(#portraitLight)" role="img" aria-label="Photo of the smiling lead dentist"/>

    <!-- contact panel -->
    <rect x="367" y="400" width="366" height="450" fill="var(--brand-red)"/>
    <rect x="392" y="440" width="316" height="180" rx="4" fill="url(#mapTone)" stroke="#ffffff" stroke-width="4" role="img" aria-label="Street map showing the practice location"/>
    <g fill="var(--brand-red)" transform="translate(0,150)">
      <rect x="508" y="2" width="20" height="14" rx="2"/>
      <path d="M509,4 L518,11 L527,4" stroke="#fff" stroke-width="1.6" fill="none"/>
      <line x1="538" y1="0" x2="538" y2="18" stroke="var(--brand-red)" stroke-width="1.5"/>
      <path d="M550,0 a7,7 0 0 1 7,7 c0,5 -7,11 -7,11 c0,0 -7,-6 -7,-11 a7,7 0 0 1 7,-7 z"/>
      <circle cx="550" cy="7" r="2.6" fill="#fff"/>
      <line x1="562" y1="0" x2="562" y2="18" stroke="var(--brand-red)" stroke-width="1.5"/>
      <circle cx="580" cy="9" r="9"/>
      <path d="M571,9 H589 M580,0 V18 M574,3 Q580,9 574,15 M586,3 Q580,9 586,15" stroke="#fff" stroke-width="1.3" fill="none"/>
    </g>

    <!-- cover panel -->
    <rect x="733" y="340" width="367" height="510" fill="var(--brand-red)"/>
    <rect x="786" y="118" width="260" height="380" rx="44" fill="url(#portraitWarm)" stroke="var(--brand-red)" stroke-width="12" role="img" aria-label="Photo of a smiling couple"/>
  </svg>

  <!-- about panel -->
  <div class="abs rank">
    <span class="rank__number">#1</span>
    <span class="rank__label">Lakeview's<br>Dental Professionals</span>
  </div>
  <p class="abs about-copy">When you visit Dr. Rowan your smile is our top priority. Our entire team is dedicated to providing the highest quality of general and esthetic dentistry while promoting and preserving the most optimum oral hygiene.</p>
  <div class="abs mission">
    <h3 class="mission__title">OUR MISSION</h3>
    <p class="mission__copy">As a practice, we are true believers that preventative care and education are the keys to optimal dental health. We strive to provide “dental health care” vs “disease care.” That’s why we focus on thorough exams – checking the overall health of your teeth and gums, performing oral cancer exams, and taking x-rays when necessary. We also know that routine cleanings, flossing, sealants, and fluoride are all helpful in preventing dental disease.</p>
  </div>

  <!-- contact panel -->
  <div class="abs contact">
    <p class="contact__call">Call us today!</p>
    <p class="contact__phone">555-014-2290</p>
    <div class="contact__details">
      <p>info@pemtrix.com</p>
      <p>1420 Harbor Ave, Lakeview,<br>Louisiana 70100</p>
      <p>www.pemtrix.com</p>
    </div>
  </div>
  <div class="abs brand brand--back"><span class="brand__dot"></span>Smileform Dental</div>

  <!-- cover panel -->
  <div class="abs brand brand--cover"><span class="brand__dot"></span>Smileform Dental</div>
  <div class="abs cover-headline">
    <p class="cover-headline__lead">We create beautiful</p>
    <p class="cover-headline__main">SMILES!</p>
  </div>
  <div class="abs cover-web">www.pemtrix.com</div>
</section>

<!-- ============ INSIDE SPREAD ============ -->
<section class="spread spread--inside" aria-label="Brochure inside">
  <svg class="spread__art" viewBox="0 0 1100 850" width="1100" height="850">
    <defs>
      <linearGradient id="groupTone" x1="0" y1="0" x2="1" y2="0">
        <stop offset="0" stop-color="#4a6f8f"/>
        <stop offset=".35" stop-color="#b58870"/>
        <stop offset=".7" stop-color="#6b4a3e"/>
        <stop offset="1" stop-color="#d9cfc6"/>
      </linearGradient>
      <linearGradient id="elderTone" x1="0" y1="0" x2="1" y2="1">
        <stop offset="0" stop-color="#bdb6b0"/>
        <stop offset=".5" stop-color="#8c5a44"/>
        <stop offset="1" stop-color="#5e3a2c"/>
      </linearGradient>
    </defs>

    <line x1="367" y1="0" x2="367" y2="850" stroke="#e2e2e2" stroke-width="1"/>
    <line x1="733" y1="0" x2="733" y2="850" stroke="#e2e2e2" stroke-width="1"/>

    <!-- intro panel -->
    <path d="M0,356 C120,344 250,366 367,348 L367,850 L0,850 Z" fill="var(--brand-red)"/>
    <path d="M0,404 C90,382 200,418 320,392 L320,850 L0,850 Z" fill="url(#elderTone)" role="img" aria-label="Photo of a smiling senior woman"/>

    <!-- price panels -->
    <rect x="367" y="0" width="733" height="330" fill="url(#groupTone)" role="img" aria-label="Photo of a large group of smiling people"/>
    <path d="M367,318 C560,282 800,300 1100,270 L1100,790 L367,790 Z" fill="var(--brand-red)"/>
    <rect x="367" y="790" width="733" height="60" fill="var(--paper)"/>
  </svg>

  <h2 class="abs services-title">Teeth<br>Whitening<br>Services</h2>
  <p class="abs services-copy">Teeth whitening is a cosmetic treatment done to improve the appearance of teeth. Teeth are whitened to remove the effects of coffee, cigarettes, and other substances that permanently stain or discolor teeth. Medications such as antibiotics like tetracycline may discolor teeth. Fluorosis, a condition caused by absorbing too much fluoride, could affect tooth color. Furthermore, aging also causes teeth to lose their bright color.</p>

  <article class="abs tier tier--basic">
    <span class="tier__badge tier__badge--basic">$10</span>
    <h3 class="tier__name">Basic</h3>
    <p class="tier__kind">Teeth whitening<br>services</p>
    <p class="tier__copy">A gentle in-office polish that lifts light surface stains and brightens your natural shade in a single short visit.</p>
  </article>

  <article class="abs tier tier--gold">
    <span class="tier__badge tier__badge--gold">$275</span>
    <h3 class="tier__name">Gold</h3>
    <p class="tier__kind">Teeth whitening<br>services</p>
    <p class="tier__copy">A two-step treatment that pairs a deep in-office session with fitted trays for home. We begin with a gentle cleaning, protect your gums, then apply a stronger gel in timed rounds. You leave with trays and gel to finish the result at your own pace over the next week.</p>
  </article>

  <article class="abs tier tier--silver">
    <span class="tier__badge tier__badge--silver">$80</span>
    <h3 class="tier__name">Silver</h3>
    <p class="tier__kind">Teeth whitening<br>services</p>
    <p class="tier__copy">Custom trays and a professional gel for home use, giving a steady lift over two weeks of easy daily wear.</p>
  </article>

  <article class="abs tier tier--diamond">
    <span class="tier__badge tier__badge--diamond">$375</span>
    <h3 class="tier__name">Diamond</h3>
    <p class="tier__kind">Teeth whitening<br>services</p>
    <p class="tier__copy">One chair-side session with a light-activated gel for a dramatic, even result you can see the same day.</p>
  </article>

  <article class="abs tier tier--platinum">
    <span class="tier__badge tier__badge--platinum">$475</span>
    <h3 class="tier__name">Platinum</h3>
    <p class="tier__kind">Teeth whitening<br>services</p>
    <p class="tier__copy">Our complete plan: in-office whitening, custom take-home trays and a follow-up touch-up kit to keep your smile bright.</p>
  </article>

  <p class="abs closing-call">Call us today!</p>
  <p class="abs closing-phone">555-014-2290</p>
</section>

</body>
</html>
```